New web/graphic designs required to improve existing ecommerce site.

Initial outline of project:
This project is for new designs to fit into areas of existing webpages - specifically:-
Objective 1 - Produce 8 home page design proposals (design for central area of page only, not whole page)
Objective 2 - Produce 5 designs for page header banners (950px x 84px images)
Objective 3 - Produce 10 designs for help guide covers (316px x 410px images)
Also, on a more general note:
Objective 4 - Review and suggest improvements for other areas website. (This may lead to further design work)
-
Introduction to the Periodical Bazaar website:
The Periodical Bazaar website is a marketplace where back-issue hobby magazines can be bought and sold, and in some cases downloaded & viewed in digital form. The ‘sellers’ of the magazines will be both traders and private individuals. Trade sellers will also be able to sell magazine subscriptions and have ‘Promotion Pages’ about themselves and/or their magazine titles on the site. Other forms of advertising will also be available on the site for any commercial advertisers who want it, particularly for companies supplying the various hobbies covered.
Users of the website can locate magazines of interest to them by browsing through the hobby / category sections of the site, or by doing keyword searches for issues containing articles on specific topics.
The site is split-up into sections dealing with magazines about specific hobby subjects – ie., cars, motorbikes, railway, aviation, boating etc. Although part of the larger site, each of these sections is largely self-contained, with many users only ever browsing in the section related to their hobby. As such, each section effectively has it’s own home page, which will duplicate much of the information shown on the main home page. These multiple ‘section home pages’ will be promoted in their own right via URLs specific to that hobby. Currently there are 8 sections, but this number is expected to increase as the site grows.
This website is still being developed, but is close to launch; as such the website is fully functional but a lot of content is missing - please bear this in mind when viewing the site, and feel free to ask for clarification if anything is unclear.
The new website is currently at: http://www2.periodicalbazaar.co.uk
This website will replace several existing sites:-
http://www.periodicalbazaar.co.uk
http://www.twowheel-quarterlies.co.uk
http://www.skyward-quarterlies.co.uk
http://www.drivezines.co.uk
http://www.trackside-quarterlies.co.uk
http://www.scalecraft-quarterlies.co.uk
-
Design notes:
The overall design is fairly conventional and very much ‘functionality’ driven, the website being at it’s heart an ecommerce system with some fairly complex features. Nevertheless I want the site to appear simple and modern in appearance, being somewhere between an ‘all style’ Web 2.0-type site (eg. tastely.io), and an ‘all function’ conventional trading site (eg. Brindle, Vendo etc). A good example of a style of site which I would like to emulate is PostParrot – a complex and large site made to look friendly and approachable by the use of simple, clear design, bold colour and a sense of humour.
To explain further what is required I have prepared various image documents which include more detailed notes on the various objectives for this project. There is a lot of information in these documents - please read them carefully:-
Objective 1:
- Produce 1 'Main Home Page' design proposal
- Produce 8 'Section Home Page' design proposals - one each for these sections: Railway, Boating, Aviation, Cycling, Automotive, Motorcycling, Men's Lifestyle, Modelling
More information on Objective 1 is given in these image documents:
http://www.filecove.net/Home_Page_Designs-Purpose.gif
http://www.filecove.net/Home_Page_Designs-Areas.gif
http://www.filecove.net/Section_Home_Pages-1.gif
http://www.filecove.net/Section_Home_Pages-2.gif
-
Objective 2:
- Produce 5 designs for page header banners (950px x 84px images)
More information on Objective 2 is given in this image document:
http://www.filecove.net/Page_Header_Banners.gif
-
Objective 3:
- Produce 10 designs for help guide covers (316px x 410px images)
http://www.filecove.net/Help_Guide_Covers.gif
-
Objective 4:
- Review and suggest improvements for other areas website
I would like the designer to spend some time looking at the whole of the current website, and suggest any areas that can be improved. I am not looking for a wholesale re-design - the overall layout of the site and major design elements such as the navigation system - are essentially fixed - however, many graphical elements can be changed, as can any text content (including text content within the navigation system).
Improvements which are suggested may lead to additional design work either as part of this project, or as subsequent projects in their own right.
-
Designers are very welcome to contact me to discuss any aspect of this project, or if more information is required about the website or the designs required.
I'm happy to guarantee this project in due course, if there is positive reaction to the project from potential designers interested in submitting designs. This is the second project I have run on SketchGuild - the first one was successful and resulted in the Flash animation that is currently on the homepage of the website.
UPDATE 11/10/11:
I've created some new documents to illustrate the sort of designs I am looking for for the Main Home Page and Section Home Pages:
Very rough examples of the sort of style I am looking for:
http://www.filecove.net/Rough_Main_Home_Page_1.jpg
http://www.filecove.net/Rough_Main_Home_Page_2.jpg
http://www.filecove.net/Rough_Main_Home_Page_3.jpg
http://www.filecove.net/Rough_Main_Home_Page_4.jpg
http://www.filecove.net/Rough_Main_Home_Page_5.jpg
http://www.filecove.net/Rough_Section_Home_Page.jpg
http://www.filecove.net/Rough_Section_Home_Page_2.jpg
Detailed document showing exact content required for the Main Home Page and each Section Home Page:
http://www.filecove.net/Home_Page_Content.gif
Mainly male, age 20 - 60. Not necessarily 'web savvy' or design-conscious
Advertising

```html
<!DOCTYPE html>
<html lang="en">
<head>
<meta charset="utf-8">
<title>Page Header Banners – Periodical Bazaar</title>
<link rel="stylesheet" href="https://fonts.googleapis.com/css2?family=Poppins:wght@700&family=Arimo:wght@400;700&family=Didact+Gothic&display=swap">
<style>
  :root {
    --page-bg: #ffffff;
    --ink: #111111;
    --bubble: #ffffff;
    --link: #1a6fd6;
    --mascot-skin: #f2c9a0;
    --mascot-cap: #a9c3d6;
    --cyan-dark: #137f8c;
    --cyan-light: #00def0;
    --blue-dark: #0b5f93;
    --blue-light: #0aa2ef;
    --red-dark: #7f0c02;
    --red-light: #ff1c00;
    --lime-dark: #6f7d00;
    --lime-light: #d9f300;
    --gold-dark: #7d6500;
    --gold-light: #f2d200;
  }
  * { box-sizing: border-box; margin: 0; padding: 0; }
  html, body { width: 1200px; height: 900px; overflow: hidden; background: var(--page-bg); }
  .sheet { position: relative; width: 1200px; height: 900px; }

  .banner {
    position: absolute;
    left: 111px;
    width: 950px;
    height: 84px;
    border-radius: 5px;
    overflow: hidden;
  }
  .banner--cyan  { background: linear-gradient(180deg, var(--cyan-dark) 0%, var(--cyan-light) 60%, var(--cyan-light) 85%, var(--cyan-dark) 100%); }
  .banner--blue  { background: linear-gradient(180deg, var(--blue-dark) 0%, var(--blue-light) 60%, var(--blue-light) 85%, var(--blue-dark) 100%); }
  .banner--red   { background: linear-gradient(180deg, var(--red-dark) 0%, var(--red-light) 60%, var(--red-light) 85%, var(--red-dark) 100%); }
  .banner--lime  { background: linear-gradient(180deg, var(--lime-dark) 0%, var(--lime-light) 60%, var(--lime-light) 85%, var(--lime-dark) 100%); }
  .banner--gold  { background: linear-gradient(180deg, var(--gold-dark) 0%, var(--gold-light) 60%, var(--gold-light) 85%, var(--gold-dark) 100%); }

  .banner__title {
    position: absolute;
    top: 22px;
    font-family: "Poppins", sans-serif;
    font-weight: 700;
    font-size: 31px;
    line-height: 40px;
    letter-spacing: 0.5px;
    color: var(--ink);
    text-transform: uppercase;
    white-space: nowrap;
  }

  .banner__mascot {
    position: absolute;
    left: 369px;
    top: 0;
    width: 120px;
    height: 84px;
    background: linear-gradient(180deg, var(--mascot-cap) 0%, var(--mascot-skin) 45%, var(--mascot-skin) 75%, var(--mascot-cap) 100%);
    border-radius: 40px 40px 0 0;
    opacity: 0.95;
  }

  .banner__bubble {
    position: absolute;
    left: 454px;
    top: 8px;
    width: 408px;
    height: 68px;
    background: var(--bubble);
    border-radius: 10px;
    color: var(--ink);
  }
  .banner__bubble--wide { width: 465px; }

  .bubble__heading {
    font-family: "Arimo", sans-serif;
    font-weight: 700;
    font-size: 11px;
    letter-spacing: 0.2px;
  }
  .bubble__text {
    font-family: "Arimo", sans-serif;
    font-size: 12px;
  }
  .bubble__text--small { font-size: 10px; line-height: 13px; }
  .bubble__link { color: var(--link); text-decoration: none; font-family: "Arimo", sans-serif; font-size: 12px; }
  .bubble__lorem {
    font-family: "Didact Gothic", sans-serif;
    font-size: 11.3px;
    line-height: 14.5px;
    letter-spacing: 0.2px;
  }
</style>
</head>
<body>
<main class="sheet">

  <section class="banner banner--cyan" style="top:90px">
    <h2 class="banner__title" style="left:32px">Login - Register</h2>
    <div class="banner__mascot" role="img" aria-label="Cartoon mascot in a grey cap holding up the message board"></div>
    <div class="banner__bubble" style="padding:12px 0 0 51px">
      <p class="bubble__heading">WELCOME, NEW USER</p>
      <p class="bubble__text" style="margin-top:10px">Simply fill in your details below to create your account!</p>
    </div>
  </section>

  <section class="banner banner--cyan" style="top:215px">
    <h2 class="banner__title" style="left:32px">Login - Register</h2>
    <div class="banner__mascot" role="img" aria-label="Cartoon mascot in a grey cap holding up the message board"></div>
    <div class="banner__bubble banner__bubble--wide" style="padding:10px 8px 0 9px">
      <p class="bubble__text bubble__text--small">&nbsp;Register to get the most from &nbsp;Magazine website, you can create a &nbsp;profile to share advice on the forum, enter competitions and comment on articles, plus receive our e-newsletter and get the latest news, offers and show updates direct to your inbox.<br>Simply fill in your details below to create your account!</p>
    </div>
  </section>

  <section class="banner banner--blue" style="top:339px">
    <h2 class="banner__title" style="left:59px">Help Center</h2>
    <div class="banner__mascot" role="img" aria-label="Cartoon mascot in a grey cap holding up the message board"></div>
    <div class="banner__bubble" style="padding:13px 0 0 26px">
      <p class="bubble__heading">WELCOME TO HELP CENTER,</p>
      <p class="bubble__text" style="margin-top:4px">&nbsp;If your question isnt listed belove, please be free to contact us</p>
      <a class="bubble__link" href="mailto:support@periodicalbazaar.com" style="display:block;margin-top:3px">&nbsp;support@periodicalbazaar.com</a>
    </div>
  </section>

  <section class="banner banner--red" style="top:464px">
    <h2 class="banner__title" style="left:59px">Checkout</h2>
    <div class="banner__mascot" role="img" aria-label="Cartoon mascot in a grey cap holding up the message board"></div>
    <div class="banner__bubble" style="padding:15px 10px 0 20px">
      <p class="bubble__lorem">Lorem ipsum dolor sit amet, consectetur adipisicing elit, sed do eiusmod tempor incididunt ut labore et dolore magna aliqua. Ut enim ad minim veniam, quis nostrud exercitation</p>
    </div>
  </section>

  <section class="banner banner--lime" style="top:588px">
    <h2 class="banner__title" style="left:111px">Search</h2>
    <div class="banner__mascot" role="img" aria-label="Cartoon mascot in a grey cap holding up the message board"></div>
    <div class="banner__bubble" style="padding:15px 10px 0 20px">
      <p class="bubble__lorem">Lorem ipsum dolor sit amet, consectetur adipisicing elit, sed do eiusmod tempor incididunt ut labore et dolore magna aliqua. Ut enim ad minim veniam, quis nostrud exercitation</p>
    </div>
  </section>

  <section class="banner banner--gold" style="top:713px">
    <h2 class="banner__title" style="left:100px">My Mags</h2>
    <div class="banner__mascot" role="img" aria-label="Cartoon mascot in a grey cap holding up the message board"></div>
    <div class="banner__bubble" style="padding:15px 10px 0 20px">
      <p class="bubble__lorem">Lorem ipsum dolor sit amet, consectetur adipisicing elit, sed do eiusmod tempor incididunt ut labore et dolore magna aliqua. Ut enim ad minim veniam, quis nostrud exercitation</p>
    </div>
  </section>

</main>
</body>
</html>
```